Packaging For 50 Kg Bags for Fertilizer

Packaging for compound fertilizer for use in Cambodia, 6 products in total. I am looking for refreshed design which reflect the functionality of the fertilizer in question. The current design as attached is crowded and does not reflect the purpose of the fertilizer.
1.DUX 47- Increase in harvest in particular fruits , or fruit vegetable such as Tomatoes,Chili, etc.
2.DUX 206 Ultra Field Crest, as name implied, Special formular to increase yield of Paddy Harvest.
3.DUX 315, Prime Mixwell - A Generic fertilizer,
4.DUX 452, Ultra Sapline Crest - special formulation for rubber Tree.
5.DUX 579, Prime Kestra- for growth of young plant,
6.DUX 694, similar to DUX 47.
Attached is existing pakaging which the Cambodian wording is a requirement. Also there is an attachment of our logo.
Farmers
Agriculture

```html
<!DOCTYPE html>
<html lang="en">
<head>
<meta charset="utf-8">
<title>DUX 47 – 50 kg Fertilizer Bag</title>
<link href="https://fonts.googleapis.com/css2?family=Arimo:wght@700&family=Roboto+Condensed:wght@700&display=swap" rel="stylesheet">
<style>
  :root {
    --backdrop: #e9ece6;
    --bag-white: #ffffff;
    --banner-orange: #f6ae3c;
    --stitch: #ffffff;
    --band-green: #9bc64a;
    --band-edge: #8a2a1c;
    --deep-green: #1f6a32;
    --brand-green: #17a04a;
    --ink: #111111;
    --root-brown: #7a4a2a;
  }
  * { margin: 0; padding: 0; box-sizing: border-box; }
  html, body { width: 1084px; height: 1200px; overflow: hidden; background: var(--backdrop); }
  .bag-face {
    position: absolute; left: 182px; top: 40px; width: 720px; height: 1120px;
    background: var(--bag-white);
    font-family: "Arimo", Arial, sans-serif;
    color: var(--ink);
    box-shadow: 0 2px 10px rgba(0,0,0,0.08);
  }
  .brand-banner { position: absolute; left: 222px; top: 0; width: 276px; height: 352px; }
  .brand-name {
    position: absolute; left: 222px; top: 258px; width: 276px;
    display: flex; align-items: center; justify-content: center; gap: 10px;
    font-size: 27px; color: #3a2a1a;
  }
  .brand-square { width: 22px; height: 22px; background: var(--brand-green); }
  .product-band {
    position: absolute; left: 0; top: 380px; width: 720px; height: 212px;
    background: var(--band-green);
  }
  .product-band::before, .product-band::after {
    content: ""; position: absolute; left: 0; width: 720px; height: 10px;
    background: radial-gradient(circle at 8px 0, var(--bag-white) 5px, transparent 5.5px) 0 0 / 16px 10px repeat-x;
  }
  .product-band::before { top: 0; }
  .product-band::after { bottom: 0; transform: scaleY(-1); }
  .band-rule { position: absolute; left: 0; width: 720px; height: 3px; background: var(--band-edge); }
  .band-rule.top { top: 18px; }
  .band-rule.bottom { bottom: 18px; }
  .product-code {
    position: absolute; left: 0; top: 30px; width: 720px; text-align: center;
    font-size: 104px; line-height: 1; color: var(--deep-green); letter-spacing: 2px;
  }
  .code-rule { position: absolute; left: 178px; top: 128px; width: 364px; height: 3px; background: var(--deep-green); }
  .product-name {
    position: absolute; left: 0; top: 134px; width: 720px; text-align: center;
    font-family: "Roboto Condensed", "Arial Narrow", sans-serif;
    font-size: 56px; line-height: 1; color: var(--deep-green);
  }
  .roots-art {
    position: absolute; left: 60px; top: 592px; width: 600px; height: 96px;
    background: linear-gradient(180deg, rgba(122,74,42,0.55), rgba(122,74,42,0.15));
  }
  .tagline {
    position: absolute; left: 0; top: 696px; width: 720px; text-align: center;
    font-family: "Roboto Condensed", "Arial Narrow", sans-serif;
    font-size: 44px; color: var(--deep-green);
  }
  .tagline-rule { position: absolute; left: 134px; top: 756px; width: 488px; height: 2px; background: var(--deep-green); }
  .nutrients {
    position: absolute; left: 0; top: 790px; width: 720px; text-align: center;
    font-family: "Roboto Condensed", "Arial Narrow", sans-serif;
    font-size: 50px; color: var(--ink);
  }
  .registration {
    position: absolute; left: 176px; width: 400px;
    font-family: "Roboto Condensed", "Arial Narrow", sans-serif;
    font-size: 24px; display: flex; gap: 10px;
  }
  .registration .number { border-bottom: 3px dotted var(--ink); padding-bottom: 2px; }
  .registration.r1 { top: 858px; }
  .registration.r2 { top: 912px; }
  .registration.r3 { top: 966px; }
  .net-weight {
    position: absolute; left: 0; top: 1040px; width: 720px; text-align: center;
    font-family: "Roboto Condensed", "Arial Narrow", sans-serif; font-size: 26px;
  }
</style>
</head>
<body>
  <div class="bag-face">
    <svg class="brand-banner" viewBox="0 0 276 352" aria-hidden="true">
      <path d="M0 0 H276 V300 L138 352 L0 300 Z" fill="var(--banner-orange)"/>
      <path d="M12 0 V292 L138 340 L264 292 V0" fill="none" stroke="var(--stitch)" stroke-width="2" stroke-dasharray="6 5"/>
    </svg>
    <div class="brand-name"><span class="brand-square"></span>VerdaNutri</div>

    <div class="product-band">
      <div class="band-rule top"></div>
      <div class="product-code">DUX 47</div>
      <div class="code-rule"></div>
      <div class="product-name">Super DUX 47</div>
      <div class="band-rule bottom"></div>
    </div>

    <div class="roots-art" role="img" aria-label="Three brown plant root illustrations spreading downward"></div>

    <div class="tagline">Harvest Booster Fertilizer</div>
    <div class="tagline-rule"></div>

    <div class="nutrients">N-12, P-6, K22+3 Mgo</div>

    <div class="registration r1"><span>MAFF</span><span class="number">FR07 4530/208 KEL-MOR</span></div>
    <div class="registration r2"><span>MAFF</span><span class="number">FR07 4530/208 KEL-MOR</span></div>
    <div class="registration r3"><span>MAFF</span><span class="number">FR07 4530/208 KEL-MOR</span></div>

    <div class="net-weight">50kg</div>
  </div>
</body>
</html>
```